WWW.VELTRONA.IT BUSINNES CARD

WE NEED A BUSINESS CARD . I HAVE A COMPANY IN ITALY NR 1 IN HAIR MEDICAL CARE AN HAIR REPLECEMENT . IN CARD I NEED WRITE WEB ADDRESS, MAIL , ADDRESS, TELEPHONE NUMBER , AND NAME
IN THE BACK SIDE I NEED MY DOCTOR LOGO .
MY WEB SITE IS WWW.VELTRONA.IT
Updates

Target Market(s)

CONSUMER B2C

Industry/Entity Type

Hair And Beauty

Contact Information for Business Card

I WANT A MEDICAL BUSINESS CARD.

Font styles to use
Other font styles liked:
• VERDANA

Colors
33a6d7
3176b5
85abd2
aedbee
eaf1f7
ffffff

Requirements
Must have
• I NEED MY LOGO AND LOGO OF DR VELTRONA

```html
<!DOCTYPE html>
<html lang="it">
<head>
<meta charset="utf-8">
<title>Veltrona – Business Card</title>
<link rel="stylesheet" href="https://fonts.googleapis.com/css2?family=Open+Sans:wght@400;600&family=Roboto+Condensed:wght@400&display=swap">
<style>
  :root {
    --card-white: #f6f6f6;
    --panel-cyan: #35d8e8;
    --brand-blue: #1d63d8;
    --wave-cyan: #3fdbe6;
    --ink: #1b1b1b;
    --icon-cyan: #22c6e0;
    --icon-frame: #c9c9c9;
    --mascot-dark: #2a2a22;
    --mascot-light: #4a6a60;
  }
  * { margin: 0; padding: 0; box-sizing: border-box; }
  html, body { width: 1200px; height: 720px; overflow: hidden; background: #ffffff; }
  .card {
    position: relative; width: 1200px; height: 720px;
    background: var(--card-white);
    font-family: "Open Sans", Verdana, sans-serif; color: var(--ink);
    overflow: hidden;
  }
  .brand {
    position: absolute; left: 46px; top: 46px;
    display: flex; align-items: center; gap: 22px;
  }
  .brand-dot { width: 62px; height: 62px; border-radius: 50%; background: var(--icon-cyan); }
  .brand-name {
    font-size: 78px; font-weight: 600; color: var(--brand-blue);
    letter-spacing: 1px; line-height: 1;
  }
  .tagline {
    position: absolute; left: 50px; top: 130px;
    font-size: 20px; letter-spacing: 1px; color: var(--brand-blue);
  }
  .wave { position: absolute; left: 0; top: 160px; }
  .person-name {
    position: absolute; left: 114px; top: 228px;
    font-size: 44px; font-weight: 400; letter-spacing: 1px;
  }
  .contact-row { position: absolute; left: 102px; display: flex; align-items: center; gap: 22px; }
  .contact-icon {
    width: 52px; height: 52px; border: 2px solid var(--icon-frame);
    display: flex; align-items: center; justify-content: center; background: #fbfbfb;
  }
  .contact-text { font-size: 30px; line-height: 36px; letter-spacing: 1px; }
  .row-phone { top: 352px; }
  .row-web { top: 446px; }
  .row-address { top: 551px; gap: 14px; }
  .row-address .contact-text { font-family: "Roboto Condensed", Arial, sans-serif; font-size: 29px; letter-spacing: 0; }
  .side-panel {
    position: absolute; left: 663px; top: 0; width: 537px; height: 720px;
    background: var(--panel-cyan);
  }
  .mascot-area {
    position: absolute; left: 52px; top: 44px; width: 452px; height: 544px;
    border-radius: 40px;
    background: radial-gradient(ellipse at 45% 55%, var(--mascot-light), var(--mascot-dark) 55%, rgba(42,42,34,0.15) 80%);
    opacity: 0.55;
  }
</style>
</head>
<body>
<main class="card">
  <div class="brand">
    <span class="brand-dot"></span>
    <span class="brand-name">Veltrona</span>
  </div>
  <p class="tagline">CURA E REINTEGRAZIONE DEI CAPELLI</p>
  <svg class="wave" width="560" height="40" viewBox="0 0 560 40">
    <path d="M8 34 Q 280 -4 552 8" fill="none" stroke="var(--wave-cyan)" stroke-width="3"/>
  </svg>

  <h1 class="person-name">DR VELTRONA</h1>

  <div class="contact-row row-phone">
    <span class="contact-icon">
      <svg width="30" height="30" viewBox="0 0 24 24"><path fill="var(--icon-cyan)" d="M3 8c0-2 4-4 9-4s9 2 9 4v2h-4V8c-1-1-3-1.5-5-1.5S8 7 7 8v2H3zM7 11h10l3 8H4z M12 13.5a2.5 2.5 0 1 0 0 5a2.5 2.5 0 0 0 0-5z"/></svg>
    </span>
    <p class="contact-text">055 4182630<br>320 5839147</p>
  </div>

  <div class="contact-row row-web">
    <span class="contact-icon">
      <svg width="32" height="32" viewBox="0 0 24 24" fill="none" stroke="var(--icon-cyan)" stroke-width="1.6"><circle cx="12" cy="12" r="9"/><ellipse cx="12" cy="12" rx="4" ry="9"/><path d="M3 12h18M4.5 7.5h15M4.5 16.5h15"/></svg>
    </span>
    <p class="contact-text">www.veltrona.it<br>info@veltrona.it</p>
  </div>

  <div class="contact-row row-address">
    <span class="contact-icon">
      <svg width="28" height="30" viewBox="0 0 24 24"><path fill="var(--icon-cyan)" d="M12 2a7 7 0 0 0-7 7c0 5 7 13 7 13s7-8 7-13a7 7 0 0 0-7-7zm0 9.5a2.5 2.5 0 1 1 0-5a2.5 2.5 0 0 1 0 5z"/></svg>
    </span>
    <p class="contact-text">R7Q2+38 Montelba, Province of Montelba</p>
  </div>

  <aside class="side-panel">
    <div class="mascot-area" role="img" aria-label="Doctor mascot illustration: a cartoon hair strand character in a white coat and blue tie giving a thumbs up, with the doctor's name beside it"></div>
  </aside>
</main>
</body>
</html>
```